Vantor Health Group Presentation Folder, for Cancer Awareness, VERY COLORFUL AND MODERN

Presentation Folder I know pretty much what i want so it should be very eazy , I have included files from folders I use now rebrand them to my new company they will be fine, no sense re creating the wheel
Full Bleed Size
20.87" x 16.68"
53 x 42.4 cm
6260 x 5004 pixels
Document Trim Size
20.75" x 16.56"
52.7 x 42.1 cm
6225 x 4969 pixels
Updates

Low design quality

Industry/Entity Type

Medical

Font styles to use
Serif

Colors

Designer to choose colors to be used in the design.

Requirements
Must have
• really I am not looking for some one to redesign, we like our folder front page and would like to see new word information added., there are two folder front pages to choose from
• So Keep the original front page and redesign the back page and the pockets
• Can Make your Design off of one of the ones I already uploaded
Nice to have
• Keep the same color schemes, Keep the original front page and redesign the back page and the pockets
Should not have
• DO not recreate the front covers, use what I gave you and just rebrand

```html
<!DOCTYPE html>
<html lang="en">
<head>
<meta charset="utf-8">
<title>Vantor Health Group – Presentation Folder</title>
<link href="https://fonts.googleapis.com/css2?family=Raleway:wght@400;500;600&family=Roboto:wght@400&display=swap" rel="stylesheet">
<style>
  :root {
    --pink: #f393a6;
    --slate: #6b6b6e;
    --slate-light: #cfd0d2;
    --ink: #5f5f62;
    --navy: #1f3f7a;
    --die: #e0485a;
    --fold: #5fcf8a;
    --paper: #ffffff;
  }
  * { margin: 0; padding: 0; box-sizing: border-box; }
  html, body { width: 1200px; height: 963px; overflow: hidden; background: var(--paper); }
  .folder { position: relative; width: 1200px; height: 963px; font-family: "Raleway", sans-serif; }
  .dieline { position: absolute; inset: 0; }
  .txt { position: absolute; }

  .quote {
    left: 444px; top: 345px; width: 150px;
    text-align: center; color: var(--ink);
    font-size: 12px; line-height: 13.8px; letter-spacing: 1px;
    white-space: nowrap;
  }
  .title {
    left: 601px; top: 123px; width: 476px; height: 39px;
    line-height: 39px; text-align: center; color: #fff;
    font-size: 19.5px; letter-spacing: 3.2px; font-weight: 500;
  }
  .subtitle {
    left: 652px; top: 163px; width: 374px; height: 29px;
    line-height: 29px; text-align: center; color: #fff;
    font-size: 10px; letter-spacing: 1.6px;
  }
  .intro {
    left: 630px; top: 199px; width: 418px;
    text-align: center; color: var(--ink);
    font-size: 10.4px; line-height: 13px;
  }
  .tagline {
    left: 601px; top: 570px; width: 476px; height: 36px;
    line-height: 36px; text-align: center; color: #fff;
    font-size: 13.5px; letter-spacing: 1.2px;
  }
  .brand {
    left: 640px; top: 620px; display: flex; align-items: center; gap: 6px;
    color: var(--navy); font-weight: 600; font-size: 11.5px; line-height: 12px; letter-spacing: .4px;
  }
  .brand-dot { width: 34px; height: 34px; border-radius: 50%; border: 3px solid var(--navy); }

  .pocket-brand {
    left: 248px; top: 682px; width: 228px;
    transform: rotate(180deg); color: #fff;
    display: flex; align-items: center; gap: 8px;
  }
  .pocket-brand .dot { width: 36px; height: 36px; border-radius: 50%; background: #fff; flex: none; }
  .pocket-brand .name { font-size: 16px; line-height: 17px; }
  .pocket-brand .sub { font-size: 8.5px; line-height: 11px; }

  .pocket-copy {
    left: 688px; top: 740px; width: 296px;
    transform: rotate(180deg); color: #fff;
    font-family: "Roboto", sans-serif; font-size: 10.2px; line-height: 13.4px;
  }
  .pocket-copy .line { display: block; text-align: justify; text-align-last: justify; white-space: nowrap; }
  .pocket-copy .line.last { text-align-last: left; }
</style>
</head>
<body>
<div class="folder">
  <svg class="dieline" width="1200" height="963" viewBox="0 0 1200 963" xmlns="http://www.w3.org/2000/svg">
    <defs>
      <linearGradient id="familyTone" x1="0" y1="0" x2="1" y2="1">
        <stop offset="0" stop-color="#9c9a98"/>
        <stop offset=".5" stop-color="#7a7774"/>
        <stop offset="1" stop-color="#b3b0ad"/>
      </linearGradient>
      <linearGradient id="tableTone" x1="0" y1="0" x2="0" y2="1">
        <stop offset="0" stop-color="#e6e4e2"/>
        <stop offset=".5" stop-color="#b8b5b2"/>
        <stop offset="1" stop-color="#8e8b88"/>
      </linearGradient>
    </defs>

    <!-- back cover blocks -->
    <rect class="back-slate" x="125" y="178" width="223" height="416" fill="var(--slate)"/>
    <rect class="back-pink" x="327" y="234" width="104" height="330" fill="var(--pink)"/>
    <rect class="back-photo" x="128" y="292" width="306" height="302" fill="url(#familyTone)" role="img" aria-label="Black and white photo of a smiling multi-generation family"/>
    <rect class="back-band" x="125" y="594" width="476" height="12" fill="var(--slate)"/>

    <!-- front cover blocks -->
    <rect class="front-title-bar" x="601" y="123" width="476" height="39" fill="var(--pink)"/>
    <rect class="front-sub-bar" x="652" y="163" width="374" height="29" fill="#9a9a9d"/>
    <rect class="front-photo" x="601" y="260" width="476" height="310" fill="url(#tableTone)" role="img" aria-label="Black and white photo of a family sharing a meal at an outdoor table"/>
    <rect class="front-band" x="601" y="570" width="476" height="36" fill="var(--slate)"/>

    <!-- left pocket -->
    <path class="pocket-left" d="M128 669 H598 L564 864 Q558 893 536 893 H128 Z" fill="var(--slate)"/>
    <rect x="128" y="669" width="32" height="224" fill="var(--slate-light)"/>
    <g class="card-slits" stroke="#fff" stroke-width="1">
      <line x1="272" y1="760" x2="302" y2="730"/>
      <line x1="420" y1="730" x2="450" y2="760"/>
      <line x1="272" y1="804" x2="302" y2="834"/>
      <line x1="420" y1="834" x2="450" y2="804"/>
    </g>

    <!-- right pocket -->
    <path class="pocket-right" d="M604 669 H1074 V893 H666 Q644 893 638 864 Z" fill="var(--slate)"/>
    <rect x="1042" y="669" width="32" height="224" fill="var(--slate-light)"/>

    <!-- fold lines -->
    <g stroke="var(--fold)" stroke-width="1" stroke-dasharray="3 2" fill="none">
      <line x1="125" y1="74" x2="125" y2="669"/>
      <line x1="601" y1="74" x2="601" y2="669"/>
      <line x1="1077" y1="74" x2="1077" y2="669"/>
      <line x1="125" y1="669" x2="1077" y2="669"/>
    </g>

    <!-- cut line -->
    <path class="cut" fill="none" stroke="var(--die)" stroke-width="1"
      d="M87 76 L125 74 H1077 L1115 76 V430 A19 19 0 0 0 1115 468 V660 L1077 669 H1074 V893 H666 Q644 893 638 864 L604 670 H598 L564 864 Q558 893 536 893 H128 V669 H125 L87 662 V468 A19 19 0 0 0 87 430 Z"/>
  </svg>

  <p class="txt quote">Don’t be Afraid of the<br>Answer: Knowledge<br>is Power and Power<br>Eradicates Fear.<br>When You are<br>Fearless, You Will<br>Make all the Right<br>Choices!</p>

  <h1 class="txt title">HEREDITARY CANCER SCREENING</h1>
  <p class="txt subtitle">DOCTORS ARE THE GATEKEEPERS TO GENETIC TESTING</p>
  <p class="txt intro">We have an obligation to help patients understand genetic risk and how testing<br>can guide heath care decisions.</p>
  <p class="txt tagline">The test you order FOR your patients</p>

  <div class="txt brand">
    <span class="brand-dot"></span>
    <span>VANTOR<br>HEALTH<br>GROUP</span>
  </div>

  <div class="txt pocket-brand">
    <span class="dot"></span>
    <div>
      <div class="name">Vantor Health Group</div>
      <div class="sub">a division of Meridian Medical Sales LLC</div>
    </div>
  </div>

  <p class="txt pocket-copy">
    <span class="line">At our state of the art, CLIA certified and COLA accredited</span>
    <span class="line">facility we perform Next Generation Sequencing (NGS)</span>
    <span class="line">based screening for mutations known to affect an</span>
    <span class="line">individual’s Risk of developing Hereditary Cancer. Results</span>
    <span class="line">from the test enable the Physician to make Better informed</span>
    <span class="line last">treatment decisions.</span>
  </p>
</div>
</body>
</html>
```